Vow-Garden-Officiants.com Rack Card Design, Double-Sided. See Attachments.

Please use the attached graphics and the contents of www.vow-garden-officiants.com to create a rack card that has the same look, feel and colors as the website, business card and existing logos. Your design must be consistent with how the business cards and website currently look.

Target Market(s)

weddings. Visit www.vow-garden-officiants.com for content and design ideas.

Requirements
Must have
• Same info as business card plus content from the website.

```html
<!DOCTYPE html>
<html lang="en">
<head>
<meta charset="utf-8">
<title>Vow-Garden-Officiants.com Rack Card</title>
<link href="https://fonts.googleapis.com/css2?family=Playfair+Display:ital,wght@0,400;1,700&family=Montserrat:wght@400;500&family=Inter:wght@700&display=swap" rel="stylesheet">
<style>
:root{
  --stage:#505356;
  --card-light:#f6f6f6;
  --card-mid:#e2e2e2;
  --ink:#2b2b2b;
  --gold:#b08620;
  --gold-light:#c9a03a;
  --gold-dark:#8a6512;
  --band:#141414;
  --tile-cap:#262626;
  --white:#ffffff;
}
*{margin:0;padding:0;box-sizing:border-box}
html,body{width:1200px;height:1082px;overflow:hidden;background:var(--stage)}
.stage{position:relative;width:1200px;height:1082px}
.card{position:absolute;top:174px;width:391px;height:850px;overflow:hidden;
  background:radial-gradient(ellipse at 50% 40%,var(--card-light) 0%,var(--card-mid) 100%);
  box-shadow:0 6px 18px rgba(0,0,0,.35)}
.card--front{left:228px}
.card--back{left:640px}
.brand-head{position:absolute;top:52px;left:0;width:100%;text-align:center;
  font-family:'Playfair Display',serif;font-weight:400;font-size:27px;color:var(--ink)}
.photo{position:absolute;left:25px;top:136px;width:339px;height:252px;border:3px solid var(--white);
  background:linear-gradient(180deg,#8f9aa0 0%,#a9b0ad 35%,#6e7b55 60%,#6a5d48 100%);
  box-shadow:0 8px 8px -6px rgba(0,0,0,.35)}
.title{position:absolute;left:0;width:100%;text-align:center;font-family:'Playfair Display',serif;
  font-style:italic;font-weight:700;color:var(--gold);line-height:1.15}
.title--front{top:412px;font-size:28px}
.title--back{top:141px;font-size:28px}
.pill{position:absolute;left:50%;transform:translateX(-50%);border-radius:20px;text-align:center;
  background:linear-gradient(90deg,var(--gold-dark),var(--gold-light) 50%,var(--gold-dark));
  font-family:'Inter',sans-serif;font-weight:700;color:#111}
.pill--tag{top:494px;width:278px;height:21px;line-height:21px;font-size:11px}
.pill--note{top:222px;width:263px;height:38px;font-size:10.5px;line-height:13px;padding-top:6px}
.intro{position:absolute;left:25px;top:527px;width:341px;font-family:'Montserrat',sans-serif;
  font-size:10px;line-height:12.2px;color:var(--ink);text-align:justify;text-align-last:center}
.seal{position:absolute;left:0;width:100%;text-align:center;font-family:'Playfair Display',serif;
  color:var(--ink)}
.seal__dot{display:block;margin:0 auto 8px;border-radius:50%;background:var(--ink)}
.seal--front{top:640px;font-size:18px}
.seal--front .seal__dot{width:46px;height:46px}
.seal--back{top:672px;font-size:14px}
.seal--back .seal__dot{width:36px;height:36px}
.contact-band{position:absolute;left:0;bottom:0;width:100%;height:81px;background:var(--band);
  border-top:2px solid var(--gold)}
.pill--address{top:759px;width:280px;height:21px;line-height:21px;font-family:'Montserrat',sans-serif;
  font-weight:500;font-size:11px;z-index:2}
.contact{position:absolute;left:0;top:789px;width:100%;text-align:center;font-family:'Montserrat',sans-serif;
  font-size:13px;line-height:16.5px;color:var(--white)}
.services{position:absolute;left:38px;top:285px;width:315px;display:grid;
  grid-template-columns:155px 155px;column-gap:5px;row-gap:16px}
.service{height:107px;border:1px solid #111;background:var(--tile-cap);display:flex;flex-direction:column}
.service__img{height:71px}
.service__cap{flex:1;text-align:center;padding-top:5px}
.service__title{font-family:'Playfair Display',serif;font-style:italic;font-size:7.5px;color:var(--gold)}
.service__sub{font-family:'Montserrat',sans-serif;font-size:6.5px;color:var(--white);margin-top:4px}
.img-floral{background:linear-gradient(135deg,#7a6a60,#efe6d4 55%,#c9b79a)}
.img-camera{background:linear-gradient(90deg,#f2f2f2 0%,#1c1c1c 45%,#e8e8e8 80%,#9fb5a0)}
.img-makeup{background:linear-gradient(135deg,#f4f2ee,#b97d95 45%,#6f9a3a)}
.img-car{background:linear-gradient(180deg,#5d7f48,#9cb0c4 50%,#e9ecef)}
.img-reception{background:linear-gradient(135deg,#6d4a2c,#d9b98a 50%,#8a6b4a)}
.img-sunset{background:linear-gradient(180deg,#e07a2e,#3a2418 50%,#c85a1e 75%,#2a2320)}
.page-label{position:absolute;top:1040px;width:391px;text-align:center;font-family:'Inter',sans-serif;
  font-weight:700;font-size:19px;color:var(--white);letter-spacing:.5px}
</style>
</head>
<body>
<div class="stage">

  <section class="card card--front">
    <div class="brand-head">Vow-Garden-Officiants.com</div>
    <div class="photo" role="img" aria-label="Photo of a couple walking hand in hand on a country path beneath a rustic wedding arch"></div>
    <h1 class="title title--front">Welcome to Marisol's<br>Vow-Garden-Officiants.com</h1>
    <div class="pill pill--tag">MORE THAN JUST A MARRIAGE OFFICIANT</div>
    <p class="intro">I've always had a deep passion for organizing and planning, and I believe that every special event deserves to be stunning. With this philosophy in mind I founded Vow-Garden-Officiants.com in 2020, and have since gained many valuable connections with industry-leading experts and vendors. I'll work day and night to guarantee that your next event will be filled with unforgettable moments.</p>
    <div class="seal seal--front"><span class="seal__dot"></span>Vow-Garden-Officiants.com</div>
    <div class="pill pill--address">214 Orchard Ln, Millbrook, PA 16901, USA</div>
    <div class="contact-band"></div>
    <div class="contact">(555) 014-2387<br>Marisol@Vow-Garden-Officiants.com<br>www.vow-garden-officiants.com</div>
  </section>

  <section class="card card--back">
    <div class="brand-head">Vow-Garden-Officiants.com</div>
    <h2 class="title title--back">Professional Network<br>of Related Services</h2>
    <div class="pill pill--note">Reduce Your Stress and Save Time. Let's Use<br>My Network of Professional Providers.</div>
    <div class="services">
      <div class="service"><div class="service__img img-floral" role="img" aria-label="Bouquet of cream roses"></div>
        <div class="service__cap"><div class="service__title">Floral Arrangement Coordination</div><div class="service__sub">Perfectly Planned</div></div></div>
      <div class="service"><div class="service__img img-camera" role="img" aria-label="Camera lens held by a photographer"></div>
        <div class="service__cap"><div class="service__title">Professional Photographer Coordination</div><div class="service__sub">Stunning and Memorable</div></div></div>
      <div class="service"><div class="service__img img-makeup" role="img" aria-label="Makeup products beside tulips"></div>
        <div class="service__cap"><div class="service__title">Hair &amp; Makeup Coordination</div><div class="service__sub">Timely &amp; Convenient</div></div></div>
      <div class="service"><div class="service__img img-car" role="img" aria-label="Bridal bouquet held from a limousine window"></div>
        <div class="service__cap"><div class="service__title">From Here to There to There.</div><div class="service__sub">Classy, Luxurious and Convenient.</div></div></div>
      <div class="service"><div class="service__img img-reception" role="img" aria-label="Restaurant tables set for a small reception"></div>
        <div class="service__cap"><div class="service__title">Coordination of Small Receptions.</div><div class="service__sub">Restaurants &amp; Wineries</div></div></div>
      <div class="service"><div class="service__img img-sunset" role="img" aria-label="Boat on a lake at sunset"></div>
        <div class="service__cap"><div class="service__title">You Can Event Sail Away!</div><div class="service__sub">Charters by Captain Rowan Ellery</div></div></div>
    </div>
    <div class="seal seal--back"><span class="seal__dot"></span>Vow-Garden-Officiants.com</div>
    <div class="pill pill--address">214 Orchard Ln, Millbrook, PA 16901, USA</div>
    <div class="contact-band"></div>
    <div class="contact">(555) 014-2387<br>Marisol@Vow-Garden-Officiants.com<br>www.vow-garden-officiants.com</div>
  </section>

  <div class="page-label" style="left:228px">FRONT PAGE</div>
  <div class="page-label" style="left:640px">BACK PAGE</div>
</div>
</body>
</html>
```